Sales and service sticker for external product

Transparent backing

Sales and service sticker to be positioned on a boiler

Contains logo
Sales and Service
Phone number: 0412983561
Website: www.calvertheat.com.au
Email: info@calvertheat.com.au

Attached photo of logo and product
I’m open to suggestion with the size and positioning of the sticker

```html
<!DOCTYPE html>
<html lang="en">
<head>
<meta charset="utf-8">
<title>Calvert Heat – Sales and Service Stickers</title>
<link href="https://fonts.googleapis.com/css2?family=Nunito+Sans:wght@700;800&family=Questrial&display=swap" rel="stylesheet">
<style>
  :root {
    --orange: #f47f20;
    --charcoal: #3d3c3e;
    --slate: #58585a;
    --silver: #bcbcbe;
    --white: #ffffff;
    --edge: #c9c9cb;
  }
  * { box-sizing: border-box; margin: 0; padding: 0; }
  html, body { width: 848px; height: 1200px; overflow: hidden; background: var(--white); }
  body { position: relative; font-family: "Nunito Sans", Arial, sans-serif; }

  .sticker {
    position: absolute; left: 122px; width: 609px; height: 179px;
    border-radius: 11px; overflow: hidden;
  }
  .sticker--light { top: 214px; background: var(--white); border: 1px solid var(--edge); }
  .sticker--dark { top: 413px; background: var(--charcoal); }
  .sticker--split { top: 612px; background: var(--charcoal); }
  .sticker--banded { top: 812px; background: var(--charcoal); }

  .brand {
    position: absolute; left: 0; top: 0; width: 317px; height: 100%;
    display: flex; align-items: center; justify-content: center; gap: 10px;
  }
  .brand__mark { width: 30px; height: 30px; background: var(--orange); flex: none; }
  .brand__name { font-weight: 800; font-size: 34px; letter-spacing: -0.5px; color: var(--silver); }
  .sticker--light .brand__name { color: var(--slate); }

  .divider { position: absolute; left: 317px; top: 20px; width: 1.5px; height: 139px; background: var(--slate); }
  .sticker--dark .divider { background: #8a8a8c; }

  .panel { position: absolute; left: 324px; right: 0; top: 0; bottom: 0; background: var(--orange); }
  .band-top { position: absolute; left: 324px; right: 0; top: 0; height: 27px; background: var(--orange); }
  .band-title { position: absolute; left: 324px; right: 0; top: 27px; height: 43px; background: var(--charcoal); }
  .band-body { position: absolute; left: 324px; right: 0; top: 70px; bottom: 0; background: var(--orange); }

  .service {
    position: absolute; left: 339px; top: 40px;
    font-family: "Questrial", "Century Gothic", sans-serif;
    font-size: 18.5px; letter-spacing: 3.6px; color: var(--slate);
  }
  .sticker--dark .service { color: var(--orange); }
  .sticker--split .service, .sticker--banded .service { color: var(--white); }
  .sticker--banded .service { top: 37px; }

  .contacts { position: absolute; left: 339px; top: 70px; list-style: none; }
  .sticker--banded .contacts { top: 86px; left: 338px; }
  .contacts li {
    display: flex; align-items: center; gap: 6px; height: 21.3px;
    font-weight: 700; font-size: 17.2px; letter-spacing: 0.1px; color: var(--slate);
  }
  .sticker--dark .contacts li { color: var(--silver); }
  .sticker--split .contacts li, .sticker--banded .contacts li { color: var(--charcoal); }

  .icon { width: 16px; height: 16px; flex: none; }
  .icon circle { fill: var(--orange); }
  .icon .glyph { fill: none; stroke: var(--white); stroke-width: 1.3; }
  .icon .glyph-fill { fill: var(--white); }
  .sticker--split .icon circle, .sticker--banded .icon circle { fill: var(--charcoal); }
</style>
</head>
<body>

<svg width="0" height="0" style="position:absolute" aria-hidden="true">
  <defs>
    <symbol id="icon-phone" viewBox="0 0 16 16">
      <circle cx="8" cy="8" r="8"/>
      <path class="glyph-fill" d="M3.2 7.6c1.2-2 8.4-2 9.6 0l-1.6 1.2-1.4-1.1c-1.6-.5-2.8-.5-4.6 0L3.8 8.8z"/>
      <circle class="glyph-fill" cx="8" cy="9.2" r="1.5" style="fill:#fff"/>
    </symbol>
    <symbol id="icon-mail" viewBox="0 0 16 16">
      <circle cx="8" cy="8" r="8"/>
      <rect class="glyph-fill" x="3.8" y="5.2" width="8.4" height="5.8" rx="0.8"/>
      <path d="M4.2 5.8L8 8.6l3.8-2.8" fill="none" stroke="#3d3c3e" stroke-width="0.9"/>
    </symbol>
    <symbol id="icon-web" viewBox="0 0 16 16">
      <circle cx="8" cy="8" r="8"/>
      <g class="glyph">
        <circle cx="8" cy="8" r="5" style="fill:none"/>
        <ellipse cx="8" cy="8" rx="2.2" ry="5"/>
        <path d="M3 8h10M3.8 5.4h8.4M3.8 10.6h8.4M8 3v10"/>
      </g>
    </symbol>
  </defs>
</svg>

<section class="sticker sticker--light">
  <div class="brand"><span class="brand__mark"></span><span class="brand__name">Calvert Heat</span></div>
  <div class="divider"></div>
  <p class="service">SALES AND SERVICE</p>
  <ul class="contacts">
    <li><svg class="icon"><use href="#icon-phone"/></svg>0412 9835 61</li>
    <li><svg class="icon"><use href="#icon-mail"/></svg>info@calvertheat.com.au</li>
    <li><svg class="icon"><use href="#icon-web"/></svg>www.calvertheat.com.au</li>
  </ul>
</section>

<section class="sticker sticker--dark">
  <div class="brand"><span class="brand__mark"></span><span class="brand__name">Calvert Heat</span></div>
  <div class="divider"></div>
  <p class="service">SALES AND SERVICE</p>
  <ul class="contacts">
    <li><svg class="icon"><use href="#icon-phone"/></svg>0412 9835 61</li>
    <li><svg class="icon"><use href="#icon-mail"/></svg>info@calvertheat.com.au</li>
    <li><svg class="icon"><use href="#icon-web"/></svg>www.calvertheat.com.au</li>
  </ul>
</section>

<section class="sticker sticker--split">
  <div class="brand"><span class="brand__mark"></span><span class="brand__name">Calvert Heat</span></div>
  <div class="panel"></div>
  <p class="service">SALES AND SERVICE</p>
  <ul class="contacts">
    <li><svg class="icon"><use href="#icon-phone"/></svg>0412 9835 61</li>
    <li><svg class="icon"><use href="#icon-mail"/></svg>info@calvertheat.com.au</li>
    <li><svg class="icon"><use href="#icon-web"/></svg>www.calvertheat.com.au</li>
  </ul>
</section>

<section class="sticker sticker--banded">
  <div class="brand"><span class="brand__mark"></span><span class="brand__name">Calvert Heat</span></div>
  <div class="band-top"></div>
  <div class="band-title"></div>
  <div class="band-body"></div>
  <p class="service">SALES AND SERVICE</p>
  <ul class="contacts">
    <li><svg class="icon"><use href="#icon-phone"/></svg>0412 9835 61</li>
    <li><svg class="icon"><use href="#icon-mail"/></svg>info@calvertheat.com.au</li>
    <li><svg class="icon"><use href="#icon-web"/></svg>www.calvertheat.com.au</li>
  </ul>
</section>

</body>
</html>
```